Rapidly Growing Small Management Consulting Firm seeking Letterhead/Business Proposal Template

Small Management Consulting Firm in need of Stationery/Business Proposal Template/Business Card for communicating and corresponding to formal Government Statement of Work (SOWs) Request for Proposals (RFP), general business correspondences and engagements with private industry clients. I am in need of company letterhead/stationery and proposal package of documents that follow the same theme in MS Word or a format that I can easily edit to readily respond quickly to business inquiries.

Consulting Firm small business start-up. Minority woman-owned rapidly growing consulting firm based in Washington, DC metropolitan area with a target market of the local and federal government. Would like see some area government images such as buildings or monuments. Looking for something eye-catching and creates a strong presence. The final design should communicate our numerous service offerings.

Target Market(s)

Local State, Federal Government and Private Industry clients and (Business-to-Business (B2B)

Industry/Entity Type

Management Consulting

Number of Pages Required

3 page

Font styles to use
Serif
Sans Serif
Other font styles liked:
• Arial, Calibri, Cambria and Times Roman

Colors
3176b5
ffffff
ec1f27
85abd2
cfdeed

Requirements
Must have
• WEBSITE: PLEASE TAKE A LOOK AT SOME OF THE IMAGES PROVIDED. I AM EXTREMELY INTERESTED IN IMAGE #16. IF SOMETHING LIKE THIS CAN BE DONE FOR THE WEBSITE LANDING PAGE WITH A WASHINGTON, DC OR MONUMENTAL BACKDROP OR BACKGROUND. WOULD LIKE TO USE THE IMAGE OF AFRICAN AMERICAN WOMAN IN FRONT ALONG WITH ANY OTHER DIVERSE STOCK IMAGES BEHIND HER. PLEASE USE A LIGHTER AND BRIGHTER BACKGROUND.
• FOR WEBSITE IMAGE INSPIRATION
• PLEASE TAKE A LOOK @ http://www.tendralux.com/
• http://vamplirio.net/wp-demo/lawfirm/practice-area-01/
• Website: I would like to see general information pages such as Home Page, About US, Services Offered and Careers and Contact Us pages. Must have consistent theme in line with existing Capability Statement.
• FOR COMPANY LETTERHEAD/PROPOSAL/PRESENTATION PAGES:
• MUST FOLLOW SAME THEME. MUST BE IN MS WORD OR FORM THAT CAN BE EASILY EDITABLE. PLEASE SEE UPLOADED "PROPOSAL-PRESENTATION COVER PAGE" IMAGES FOR ADDITIONAL INSPIRATION. I VERY MUCH LIKE IMAGES PPCP #4 AND PPCP#5.
• Must include a multi-use company cover page for proposals and business presentations.
• For letterhead and please incorporate existing logo into design. Company colors gray and blue. Must have the functionality to format page numbering, consistent company information throughout document in headers and footers and will need a customizable company cover page that can be used for proposals and presentations.
• Please do not make the header and footer borders too large as I have to be able to input company information into the space. Some responses have set page limits so it is very important to preserve as much space as possible.
• Please use updated company address: 482 Harrowgate Lane, Bel Alton, MD 20611
Nice to have
• Illustration of images that show professional women and minority (african-american) woman in business or professional settings. Women business owners preferably. Classic and very professional appearance. Even though we are a small firm I would like to design to give the impression and feel of doing business with a large management firm. Or large firm appeal. Also incorporate image of contract signing as our main line of business is acquisitions which is much like the services of a law firm.
• 01/21/17. Added some images of women business owner examples.
Should not have
• Misspellings, images of professionals without business attire.

```html
<!DOCTYPE html>
<html lang="en">
<head>
<meta charset="utf-8">
<title>Corvane Advisors Stationery</title>
<link rel="stylesheet" href="https://fonts.googleapis.com/css2?family=Open+Sans:wght@400;600;700&family=Dancing+Script:wght@500&display=swap">
<style>
  :root {
    --navy: #1c3f7c;
    --blue: #3176b5;
    --sky: #85abd2;
    --mist: #cfdeed;
    --paper: #ffffff;
    --ink: #3a3f47;
    --backdrop: #eef0f2;
  }
  * { box-sizing: border-box; margin: 0; padding: 0; }
  html, body { width: 1200px; height: 809px; overflow: hidden; }
  body {
    background: var(--backdrop);
    font-family: "Open Sans", Arial, sans-serif;
    color: var(--ink);
    position: relative;
  }

  .brand { display: flex; align-items: center; gap: 6px; color: var(--navy); font-weight: 600; letter-spacing: 0.12em; text-transform: uppercase; }
  .brand-mark { width: 10px; height: 10px; background: var(--navy); }
  .brand--light { color: var(--paper); }
  .brand--light .brand-mark { background: var(--paper); }

  /* Letterhead */
  .letterhead {
    position: absolute; left: 70px; top: 34px;
    width: 523px; height: 740px;
    background: var(--paper);
    box-shadow: 0 2px 10px rgba(0,0,0,0.08);
  }
  .letterhead .brand { position: absolute; top: 46px; left: 0; right: 0; justify-content: center; font-size: 15px; }
  .letter-body { position: absolute; left: 56px; right: 56px; top: 130px; font-size: 8.2px; line-height: 1.55; }
  .letter-meta { margin-bottom: 12px; }
  .letter-body p { margin-bottom: 10px; }
  .signature { font-family: "Dancing Script", cursive; font-size: 20px; color: var(--navy); margin: 4px 0 0; }
  .signer-title { margin-top: -2px; }
  .letter-footer { position: absolute; left: 56px; right: 56px; bottom: 46px; }
  .letter-footer .rule { height: 2px; background: var(--navy); }
  .letter-contact { text-align: center; font-size: 7.5px; color: var(--navy); padding: 8px 0 6px; }
  .letter-band { background: var(--navy); color: var(--paper); font-size: 7.5px; text-align: center; padding: 4px 0; letter-spacing: 0.03em; }

  /* Business cards */
  .card { position: absolute; width: 320px; height: 183px; box-shadow: 0 2px 10px rgba(0,0,0,0.1); }
  .card--front { left: 700px; top: 470px; background: var(--navy); color: var(--paper); }
  .card--front .brand { position: absolute; top: 66px; left: 0; right: 0; justify-content: center; font-size: 15px; }
  .card-services { position: absolute; top: 100px; left: 30px; right: 30px; text-align: center; font-size: 6.5px; color: var(--mist); line-height: 1.5; }
  .card--back { left: 780px; top: 200px; background: var(--paper); }
  .card--back .brand { position: absolute; top: 40px; left: 34px; font-size: 13px; }
  .card-name { position: absolute; left: 34px; top: 110px; font-size: 8.5px; font-weight: 700; color: var(--navy); letter-spacing: 0.05em; }
  .card-role { position: absolute; left: 34px; top: 123px; font-size: 6.5px; color: var(--ink); }
  .card-contact { position: absolute; right: 22px; top: 34px; list-style: none; font-size: 6.5px; color: var(--ink); }
  .card-contact li { display: flex; align-items: center; gap: 5px; margin-bottom: 6px; }
  .card-contact svg { width: 9px; height: 9px; }
  .card-band { position: absolute; left: 0; right: 0; bottom: 20px; height: 13px; background: var(--navy); color: var(--paper); font-size: 6px; text-align: center; line-height: 13px; }
  .card-rule { position: absolute; left: 0; right: 0; bottom: 36px; height: 1.5px; background: var(--navy); }
</style>
</head>
<body>

<section class="letterhead">
  <div class="brand"><span class="brand-mark"></span>Corvane Advisors</div>
  <div class="letter-body">
    <div class="letter-meta">
      November 1, 2013<br>
      Mr. Dalton Reeve<br>
      1234 Fenwick Row Lane<br>
      Easton, MD 21601
    </div>
    <p>Dear Mr. Reeve,</p>
    <p>The first paragraph of a typical business letter is used to state the main point of the letter. Begin with a friendly opening; then quickly transition into the purpose of your letter. Use a couple of sentences to explain the purpose, but do not go in to detail until the next paragraph.</p>
    <p>Beginning with the second paragraph, state the supporting details to justify your purpose. These may take the form of background information, statistics or first-hand accounts. A few short paragraphs within the body of the letter should be enough to support your reasoning. Finally, in the closing paragraph, briefly restate your purpose and why it is important. If the purpose of your letter is related to your employment, consider ending your letter with your contact information and title if not included on letterhead.</p>
    <p>Finally, in the closing paragraph, briefly restate your purpose and why it is important. If the purpose of your letter is related to your employment, consider ending your letter with your contact information and title if not included on letterhead. However if the purpose is informational, think about closing with gratitude for the reader's time.</p>
    <p>Sincerely,</p>
    <div class="signature">Maren Cole</div>
    <div class="signer-title">President</div>
  </div>
  <footer class="letter-footer">
    <div class="rule"></div>
    <div class="letter-contact">202-555-0148 &nbsp;|&nbsp; lcorvane@corvaneadvisors.com &nbsp;|&nbsp; www.corvaneadvisors.com</div>
    <div class="letter-band">Specializing in Full Lifecycle Acquisition Support &amp; Consulting Services</div>
  </footer>
</section>

<section class="card card--back">
  <div class="brand"><span class="brand-mark"></span>Corvane</div>
  <ul class="card-contact">
    <li><svg viewBox="0 0 10 10"><circle cx="5" cy="5" r="5" fill="#1c3f7c"/><path d="M3.3 2.8l1 1-.5.6a3 3 0 001.8 1.8l.6-.5 1 1-.6.8C4.9 7.3 2.7 5.1 2.5 3.4z" fill="#fff"/></svg>202-555-0148</li>
    <li><svg viewBox="0 0 10 10"><circle cx="5" cy="5" r="5" fill="#1c3f7c"/><rect x="2.5" y="3.3" width="5" height="3.4" fill="none" stroke="#fff" stroke-width=".7"/><path d="M2.5 3.3L5 5.3l2.5-2" fill="none" stroke="#fff" stroke-width=".7"/></svg>lcorvane@corvaneadvisors.com</li>
    <li><svg viewBox="0 0 10 10"><circle cx="5" cy="5" r="5" fill="#1c3f7c"/><circle cx="5" cy="5" r="2.6" fill="none" stroke="#fff" stroke-width=".7"/><path d="M2.4 5h5.2M5 2.4v5.2" stroke="#fff" stroke-width=".6"/></svg>www.corvaneadvisors.com</li>
  </ul>
  <div class="card-name">LORETTA J. CORVANE</div>
  <div class="card-role">President &amp; CEO</div>
  <div class="card-rule"></div>
  <div class="card-band">Full Lifecycle Acquisition Support</div>
</section>

<section class="card card--front">
  <div class="brand brand--light"><span class="brand-mark"></span>Corvane Advisors</div>
  <div class="card-services">Acquisition Planning &bull; Contract Support &bull; Cost Analysis<br>Program Management &bull; Policy Compliance</div>
</section>

</body>
</html>
```